Brand-new Pediatric Dental Practice needs a website

We are a brand-new dental practice that will specialize in treating children. We want a gorgeous and easily navigable dental practice website that would make a good first impression to potential patients and their parents. It should be modern, SEO-friendly, mobile responsive, and optimized to win new patients.

Target Market(s)

Parents

Industry/Entity Type

Healthcare/Dentistry

Coding

Coded - Design and coding required

Number of Pages Required

4 page

Requirements
Must have
• Use the Wix website building platform. 4 pages: home, meet our dentists, services, contact us
Nice to have
• has a link to our facebook, instagram

```html
<!DOCTYPE html>
<html lang="en">
<head>
<meta charset="utf-8">
<title>Maple Grove Pediatric Dentistry</title>
<link rel="stylesheet" href="https://fonts.googleapis.com/css2?family=Nunito+Sans:wght@300;400;600;700;800&family=Quicksand:wght@400;500;600&display=swap">
<style>
:root{
  --green:#3aa358;
  --green-dark:#2c8a47;
  --green-light:#86cc8f;
  --green-pale:#c9e8cc;
  --ink:#1f2326;
  --text:#5b6166;
  --muted:#8a9095;
  --bg-soft:#f2f6f7;
  --white:#ffffff;
  --charcoal:#2f3234;
}
*{margin:0;padding:0;box-sizing:border-box}
html,body{width:1200px;height:3856px;overflow:hidden}
body{font-family:"Nunito Sans",sans-serif;color:var(--text);background:var(--white);position:relative}
.abs{position:absolute}
.photo{position:absolute}
/* header */
.brand{position:absolute;display:flex;align-items:center;gap:12px}
.brand-mark{width:56px;height:56px;border-radius:50%;background:var(--green-light)}
.brand-name{font-family:"Quicksand",sans-serif;font-weight:500;color:var(--charcoal);font-size:31px;line-height:1}
.brand-sub{font-family:"Quicksand",sans-serif;font-weight:500;color:var(--charcoal);font-size:9px;letter-spacing:3.2px;margin-top:4px}
.nav a{position:absolute;top:40px;font-size:13px;color:var(--text);text-decoration:none;text-transform:uppercase}
.nav a.active{color:var(--ink)}
.nav a.active::after{content:"";position:absolute;left:0;right:0;bottom:-12px;height:3px;background:var(--green)}
.phone-btn{position:absolute;left:955px;top:30px;width:154px;height:36px;border-radius:18px;background:var(--green-light);color:#fff;font-weight:700;font-size:13px;display:flex;align-items:center;justify-content:center;gap:6px}
/* hero */
.hero-bg{position:absolute;left:0;top:0;width:1200px;height:700px;background:linear-gradient(180deg,#fff 0%,#f3f7f8 100%)}
.hero-welcome{left:100px;top:232px;font-family:"Quicksand",sans-serif;font-size:42px;color:var(--green-light);font-weight:400}
.hero-title{left:98px;top:270px;font-family:"Quicksand",sans-serif;font-size:76px;font-weight:600;color:#111;letter-spacing:-1px}
.hero-sub{left:112px;top:360px;font-size:28px;color:var(--green-light);letter-spacing:1px;font-weight:400}
.btn-solid{position:absolute;background:linear-gradient(90deg,var(--green),var(--green-light));color:#fff;font-weight:700;font-size:15px;display:flex;align-items:center;justify-content:center}
.chev{position:absolute}
/* section headings */
.section-title{position:absolute;left:0;width:1200px;text-align:center;font-size:36px;font-weight:800;color:var(--ink)}
.section-title span{color:var(--green-light);font-weight:400}
.rule{position:absolute;height:3px;background:var(--green)}
/* about */
.eyebrow{font-size:15px;color:var(--green);text-transform:uppercase}
.about-title{font-size:36px;font-weight:800;color:var(--ink)}
.about-title span{color:var(--green-light);font-weight:400}
.para{font-size:14.5px;line-height:21px;color:var(--text)}
.btn-outline{position:absolute;border:2px solid var(--green-light);color:var(--green);font-weight:700;font-size:12px;display:flex;align-items:center;justify-content:center;background:#fff;text-transform:uppercase}
.feature{position:absolute;display:flex;gap:14px;align-items:center}
.feature-icon{width:70px;height:70px;border-radius:50%;background:var(--green);display:flex;align-items:center;justify-content:center}
.feature-icon.light{background:var(--green-light)}
.feature h4{font-size:17px;font-weight:700;color:#333}
.feature p{font-size:12px;color:var(--muted);margin-top:6px}
/* services */
.services-bg{position:absolute;left:0;top:1300px;width:1200px;height:560px;background:var(--bg-soft)}
.service{position:absolute;top:1427px;width:242px;height:307px}
.service .photo{left:0;top:0;width:242px;height:185px;border-top-right-radius:40px}
.service .card{position:absolute;left:6px;right:0;top:170px;bottom:0;border:2px solid var(--green-pale);border-top:none;background:#fff;text-align:center;padding-top:40px}
.service h3{font-size:16px;font-weight:700;color:#222}
.service p{font-size:11px;line-height:18px;color:var(--muted);margin:4px 22px 0}
.service .down{position:absolute;left:50%;bottom:8px;transform:translateX(-50%)}
/* dentists */
.dentist{position:absolute}
.dentist .photo{left:0;top:0}
.dentist .info{position:absolute;background:#fff;text-align:center;box-shadow:0 2px 8px rgba(0,0,0,.08)}
.dentist .info h3{font-size:17px;font-weight:600;color:#333;margin-top:16px}
.dentist .info p{font-size:11px;line-height:16px;color:var(--muted);margin-top:4px}
.dentist.featured .info{background:var(--green-light)}
.dentist.featured .info h3,.dentist.featured .info p{color:#fff}
.dentist.featured .info h3{font-size:19px}
/* testimonials */
.testi-bg{position:absolute;left:0;top:2508px;width:1200px;height:412px;background:#eef3f5}
.testi-title{left:78px;top:2610px;font-size:32px;font-weight:800;line-height:38px;color:var(--ink)}
.testi-title .g{color:var(--green-light)}
.testi-card{position:absolute;top:2627px;width:266px;height:198px;background:#fff;box-shadow:0 2px 6px rgba(0,0,0,.12);border-bottom:3px solid var(--green-light);padding:56px 26px 0}
.testi-card .avatar{position:absolute;left:26px;top:-30px;width:70px;height:70px;border-radius:50%}
.testi-card p{font-size:11px;line-height:18px;font-style:italic;color:var(--muted)}
.testi-card h5{font-size:13px;font-weight:600;color:#222;margin-top:14px;text-transform:uppercase}
/* booking */
.book-bg{position:absolute;left:0;top:2920px;width:1200px;height:560px;background:linear-gradient(160deg,var(--green) 0%,#5eb86e 45%,#a7d9a6 100%)}
.field{position:absolute;background:#fff;border:1px solid #d8e6d9;font-size:12px;color:var(--muted);padding:22px 18px 0}
.btn-dark{position:absolute;left:510px;top:3306px;width:176px;height:44px;border-radius:22px;background:var(--charcoal);color:#fff;font-weight:800;font-size:13px;display:flex;align-items:center;justify-content:center}
/* footer */
.foot-col{position:absolute;top:3548px;border-left:2px solid var(--green-pale);padding-left:20px}
.foot-col h4{font-size:16px;font-weight:700;color:#333;margin-bottom:14px}
.foot-col li{list-style:none;font-size:13px;color:#555;line-height:28px}
.contact-row{display:flex;gap:10px;align-items:flex-start;font-size:13px;color:#555;line-height:22px;margin-bottom:6px}
.dot-ico{width:24px;height:24px;border-radius:50%;background:var(--green-light);flex:none;display:flex;align-items:center;justify-content:center}
.social{position:absolute;top:3711px;width:32px;height:32px;border-radius:50%;background:#8c8f91}
.copyright{position:absolute;left:0;top:3810px;width:1200px;text-align:center;font-size:11px;color:#555}
</style>
</head>
<body>

<div class="hero-bg"></div>

<header>
  <div class="brand" style="left:98px;top:22px">
    <div class="brand-mark"></div>
    <div>
      <div class="brand-name">maple grove</div>
      <div class="brand-sub">PEDIATRIC DENTISTRY</div>
    </div>
  </div>
  <nav class="nav">
    <a class="active" style="left:387px">About Us</a>
    <a style="left:513px">Services</a>
    <a style="left:635px">Meet our Dentists</a>
    <a style="left:832px">Contact Us</a>
  </nav>
  <div class="phone-btn">
    <svg width="13" height="13" viewBox="0 0 24 24"><path fill="#fff" d="M6.6 10.8a15 15 0 006.6 6.6l2.2-2.2c.3-.3.7-.4 1-.2 1.1.4 2.3.6 3.6.6.6 0 1 .4 1 1V20c0 .6-.4 1-1 1C10.6 21 3 13.4 3 4c0-.6.4-1 1-1h3.5c.6 0 1 .4 1 1 0 1.3.2 2.5.6 3.6.1.3 0 .7-.2 1z"/></svg>
    +1 555 014 2290
  </div>
</header>

<!-- hero -->
<section>
  <svg class="abs" style="left:540px;top:100px" width="560" height="540" viewBox="0 0 560 540">
    <path d="M110 80 A250 250 0 0 0 240 520" fill="none" stroke="#c9e8cc" stroke-width="40"/>
    <circle cx="288" cy="255" r="248" fill="none" stroke="#86cc8f" stroke-width="22"/>
  </svg>
  <div class="photo" role="img" aria-label="Smiling girl with open hands in front of a green tooth shape" style="left:590px;top:117px;width:480px;height:480px;border-radius:50%;background:radial-gradient(circle at 50% 40%,#7fc98a 0%,#3aa358 55%,#2a6b3e 100%)"></div>
  <div class="abs hero-welcome">Welcome to</div>
  <div class="abs hero-title">Maple Grove</div>
  <div class="abs hero-sub">PEDIATRIC DENTISTRY</div>
  <div class="btn-solid" style="left:113px;top:418px;width:256px;height:48px">BOOK AN APPOINTMENT</div>
  <svg class="chev" style="left:40px;top:320px" width="30" height="50"><path d="M24 4 L6 25 L24 46" fill="none" stroke="#888" stroke-width="2"/></svg>
  <svg class="chev" style="left:1148px;top:320px" width="30" height="50"><path d="M6 4 L24 25 L6 46" fill="none" stroke="#888" stroke-width="2"/></svg>
  <svg class="abs" style="left:0;top:600px" width="1200" height="110" viewBox="0 0 1200 110">
    <path d="M0 110 L0 60 C250 0 500 20 700 45 C900 70 1050 60 1200 40 L1200 110Z" fill="#fff"/>
    <path d="M0 62 C250 5 500 25 700 50 C900 75 1050 60 1200 45" fill="none" stroke="#3aa358" stroke-width="9"/>
    <path d="M200 30 C400 10 600 30 800 55" fill="none" stroke="#86cc8f" stroke-width="4"/>
  </svg>
</section>

<!-- about -->
<section>
  <div class="abs" style="left:92px;top:740px;width:178px;height:138px;border:2px solid #cfd6d9;border-right:none;border-bottom:none"></div>
  <div class="photo" role="img" aria-label="Dentist showing a young boy his teeth in a mirror" style="left:103px;top:753px;width:450px;height:325px;border-top-right-radius:50px;background:linear-gradient(135deg,#3f6fa3 0%,#9fb7c8 40%,#e9eef1 100%)"></div>
  <svg class="abs" style="left:335px;top:855px" width="250" height="250">
    <defs><pattern id="dots" width="11" height="11" patternUnits="userSpaceOnUse"><circle cx="2" cy="2" r="1.3" fill="#3aa358"/></pattern></defs>
    <rect x="220" y="0" width="28" height="245" fill="url(#dots)"/>
    <rect x="0" y="230" width="248" height="12" fill="url(#dots)"/>
  </svg>
  <div class="abs" style="left:632px;top:776px">
    <div class="eyebrow">Our Vision &amp; Mission</div>
    <div class="about-title" style="margin-top:4px"><span>ABOUT</span> MAPLE GROVE</div>
  </div>
  <div class="rule" style="left:632px;top:847px;width:84px"></div>
  <div class="abs para" style="left:632px;top:875px;width:450px">
    <p>Lorem ipsum dolor sit amet, consectetur adipiscing elit, sed do eiusmod tempor incididunt ut labore et dolore magna aliqua. Ut enim ad minim veniam, quis nostrud exercitation ullamco laboris nisi ut aliquip.Lorem ipsum dolor sit amet, do</p>
    <p style="margin-top:12px">consectetur adipiscing elit, sed do eiusmod tempor incididunt ut labore et dolore magna aliqua. Ut enim ad minim veniam</p>
  </div>
  <div class="btn-outline" style="left:632px;top:1041px;width:152px;height:42px">Learn More</div>

  <div class="feature" style="left:120px;top:1175px">
    <div class="feature-icon"><svg width="34" height="34" viewBox="0 0 24 24" fill="none" stroke="#fff" stroke-width="1.5"><circle cx="12" cy="7" r="4"/><path d="M4 22c0-5 3.5-8 8-8s8 3 8 8z"/></svg></div>
    <div><h4>Experienced Doctor</h4><p>Lorem ipsum dolor sit amet,</p></div>
  </div>
  <div class="feature" style="left:448px;top:1182px">
    <div class="feature-icon light"><svg width="32" height="32" viewBox="0 0 24 24" fill="none" stroke="#fff" stroke-width="1.6"><path d="M12 20s-7-4.4-7-10a4 4 0 017-2.6A4 4 0 0119 10c0 5.6-7 10-7 10z"/></svg></div>
    <div><h4>Friendly Doctors</h4><p>Lorem ipsum dolor sit amet, consecte</p></div>
  </div>
  <div class="feature" style="left:808px;top:1182px">
    <div class="feature-icon"><svg width="34" height="34" viewBox="0 0 24 24" fill="none" stroke="#fff" stroke-width="1.5"><path d="M12 3l2.7 5.6 6.1.9-4.4 4.3 1 6.1L12 17l-5.4 2.9 1-6.1-4.4-4.3 6.1-.9z"/></svg></div>
    <div><h4>Top Rated Clinic</h4><p>Lorem ipsum dolor sit amet, cons</p></div>
  </div>
</section>

<!-- services -->
<section>
  <div class="services-bg"></div>
  <div class="section-title" style="top:1335px"><span>OUR</span> SERVICES</div>
  <div class="rule" style="left:570px;top:1384px;width:62px"></div>

  <article class="service" style="left:100px">
    <div class="photo" role="img" aria-label="Girl in dental chair during an examination" style="background:linear-gradient(135deg,#4d7fb8,#e9d9a8)"></div>
    <div class="card"><h3>Control Examination</h3><p>Lorem ipsum dolor sit amet, con-sectetur adipiscing elit</p>
      <svg class="down" width="24" height="24"><circle cx="12" cy="12" r="10" fill="none" stroke="#3aa358" stroke-width="1.6"/><path d="M7 10 L12 15 L17 10" fill="none" stroke="#3aa358" stroke-width="1.6"/></svg></div>
  </article>
  <article class="service" style="left:357px">
    <div class="photo" role="img" aria-label="Close-up of teeth cleaning with a dental tool" style="background:linear-gradient(135deg,#3f7cc4,#e7c1b3)"></div>
    <div class="card"><h3>Teeth Cleaning</h3><p>Lorem ipsum dolor sit amet, con-sectetur adipiscing elit</p>
      <svg class="down" width="24" height="24"><circle cx="12" cy="12" r="10" fill="none" stroke="#3aa358" stroke-width="1.6"/><path d="M7 10 L12 15 L17 10" fill="none" stroke="#3aa358" stroke-width="1.6"/></svg></div>
  </article>
  <article class="service" style="left:614px">
    <div class="photo" role="img" aria-label="Hands holding a dental implant model" style="background:linear-gradient(135deg,#f1f1f1,#e8a4b4)"></div>
    <div class="card"><h3>Implantology</h3><p>Lorem ipsum dolor sit amet, con-sectetur adipiscing elit</p>
      <svg class="down" width="24" height="24"><circle cx="12" cy="12" r="10" fill="none" stroke="#3aa358" stroke-width="1.6"/><path d="M7 10 L12 15 L17 10" fill="none" stroke="#3aa358" stroke-width="1.6"/></svg></div>
  </article>
  <article class="service" style="left:871px">
    <div class="photo" role="img" aria-label="Illustrated tooth roots for root canal treatment" style="background:linear-gradient(135deg,#a8e6e3,#2fb3b3)"></div>
    <div class="card"><h3>Root Canal treatment</h3><p>Lorem ipsum dolor sit amet, con-sectetur adipiscing elit</p>
      <svg class="down" width="24" height="24"><circle cx="12" cy="12" r="10" fill="none" stroke="#3aa358" stroke-width="1.6"/><path d="M7 10 L12 15 L17 10" fill="none" stroke="#3aa358" stroke-width="1.6"/></svg></div>
  </article>

  <svg class="abs" style="left:0;top:1790px" width="1200" height="80" viewBox="0 0 1200 80">
    <path d="M0 80 L0 62 C200 20 420 0 600 20 C800 45 1000 50 1200 25 L1200 80Z" fill="#fff"/>
    <path d="M0 64 C200 22 420 2 600 22 C800 47 1000 52 1200 28" fill="none" stroke="#3aa358" stroke-width="8"/>
    <path d="M150 30 C350 5 520 8 700 30" fill="none" stroke="#86cc8f" stroke-width="4"/>
  </svg>
</section>

<!-- dentists -->
<section>
  <div class="section-title" style="top:1922px"><span>MEET</span> OUR DENTISTS</div>
  <div class="rule" style="left:577px;top:1970px;width:66px"></div>

  <article class="dentist" style="left:152px;top:2032px">
    <div class="photo" role="img" aria-label="Portrait of a female dentist holding a mirror" style="width:272px;height:272px;background:linear-gradient(135deg,#f4f4f4,#b9b9b9)"></div>
    <div class="info" style="left:12px;top:211px;width:248px;height:92px"><h3>Dentist Name</h3><p>Lorem ipsum dolor sit amet, consect-<br>etur adipiscing eli sed do</p></div>
  </article>
  <article class="dentist featured" style="left:457px;top:2012px">
    <div class="photo" role="img" aria-label="Portrait of a senior male dentist in scrubs" style="width:308px;height:310px;background:linear-gradient(135deg,#dfe6ec,#5a86b8)"></div>
    <div class="info" style="left:15px;top:241px;width:278px;height:105px"><h3>Dentist Name</h3><p>Lorem ipsum dolor sit amet, consect-<br>etur adipiscing eli sed do</p></div>
  </article>
  <article class="dentist" style="left:790px;top:2032px">
    <div class="photo" role="img" aria-label="Portrait of a female dentist with arms crossed" style="width:272px;height:272px;background:linear-gradient(135deg,#f2f2f2,#a9a9a9)"></div>
    <div class="info" style="left:14px;top:211px;width:246px;height:92px"><h3>Dentist Name</h3><p>Lorem ipsum dolor sit amet, consect-<br>etur adipiscing eli sed do</p></div>
  </article>
  <svg class="chev" style="left:78px;top:2148px" width="30" height="46"><path d="M24 4 L6 23 L24 42" fill="none" stroke="#888" stroke-width="2"/></svg>
  <svg class="chev" style="left:1110px;top:2148px" width="30" height="46"><path d="M6 4 L24 23 L6 42" fill="none" stroke="#888" stroke-width="2"/></svg>
  <div class="btn-outline" style="left:507px;top:2383px;width:230px;height:48px;border-radius:24px;font-size:14px;font-weight:600">View More Dentist</div>
</section>

<!-- testimonials -->
<section>
  <div class="testi-bg"></div>
  <div class="abs" style="left:70px;top:2545px;width:360px;height:340px;border-radius:170px 170px 40px 40px;background:rgba(255,255,255,.45)"></div>
  <div class="abs testi-title"><span class="g">WHAT OUR KIDS</span><br>PARENTS SAYS</div>
  <div class="rule" style="left:78px;top:2697px;width:70px"></div>
  <p class="abs para" style="left:75px;top:2722px;width:310px;font-size:13px">Lorem ipsum dolor sit amet, consectetur adipisc-ing elit, sed do eiusmod tempor incididun</p>

  <div class="testi-card" style="left:448px">
    <div class="avatar" role="img" aria-label="Photo of a parent with child" style="background:linear-gradient(135deg,#f2b63b,#6b3f2a)"></div>
    <p>Lorem ipsum dolor sit amet, consectetur adipiscing elit, sed do eiusmod tempor incididunt ut labore et dolore magna aliqua. Ut enim ad minim veniam,</p>
    <h5>Patient Parent Name</h5>
  </div>
  <div class="testi-card" style="left:745px">
    <div class="avatar" role="img" aria-label="Photo of a parent hugging child" style="background:linear-gradient(135deg,#e9e3de,#4a3026)"></div>
    <p>Lorem ipsum dolor sit amet, consectetur adipiscing elit, sed do eiusmod tempor incididunt ut labore et dolore magna aliqua. Ut enim ad minim veniam</p>
    <h5>Patient Parent Name</h5>
  </div>
  <div class="testi-card" style="left:1046px">
    <div class="avatar" role="img" aria-label="Photo of a family" style="background:linear-gradient(135deg,#e9ecef,#6b4b3c)"></div>
    <p>Lorem ipsum dolor sit amet, adipiscing elit, sed do eiusmod incididunt ut labore et dolore aliqua. Ut enim a</p>
    <h5>Patient Parent Name</h5>
  </div>
</section>

<!-- booking -->
<section>
  <div class="book-bg"></div>
  <div class="abs" style="left:0;top:3000px;width:1186px;text-align:center;color:#fff;font-size:15px">GET IN TOUCH</div>
  <div class="abs" style="left:0;top:3030px;width:1216px;text-align:center;color:#fff;font-size:30px;font-weight:800">BOOK AN APPOINTMENT</div>
  <div class="field" style="left:305px;top:3081px;width:290px;height:48px;padding-top:16px">First Name</div>
  <div class="field" style="left:604px;top:3081px;width:290px;height:48px;padding-top:16px">Last Name</div>
  <div class="field" style="left:305px;top:3137px;width:290px;height:48px;padding-top:16px">Email address</div>
  <div class="field" style="left:604px;top:3137px;width:290px;height:48px;padding-top:16px">Phone</div>
  <div class="field" style="left:305px;top:3193px;width:589px;height:96px;padding-top:14px">Message</div>
  <div class="btn-dark">SEND MESSAGE</div>
  <svg class="abs" style="left:0;top:3400px" width="1200" height="90" viewBox="0 0 1200 90">
    <path d="M0 90 L0 60 C200 20 420 5 620 25 C820 45 1000 40 1200 15 L1200 90Z" fill="#fff"/>
    <path d="M0 62 C200 22 420 7 620 27 C820 47 1000 42 1200 17" fill="none" stroke="#3aa358" stroke-width="8"/>
    <path d="M150 34 C350 8 520 10 720 34" fill="none" stroke="#fff" stroke-width="3"/>
  </svg>
</section>

<!-- footer -->
<footer>
  <div class="abs" style="left:125px;top:3560px;width:200px;text-align:center">
    <div style="width:84px;height:84px;border-radius:50%;background:var(--green-light);margin:0 auto 12px"></div>
    <div class="brand-name" style="font-size:33px">maple grove</div>
    <div class="brand-sub" style="font-size:10px;margin-top:4px">PEDIATRIC DENTISTRY</div>
  </div>
  <div class="social" style="left:172px"></div>
  <div class="social" style="left:212px"></div>
  <div class="social" style="left:252px"></div>

  <div class="foot-col" style="left:384px;height:150px">
    <h4>Navigation</h4>
    <ul><li>About Us</li><li>Meet Our Dentists</li><li>Our Services</li><li>Contact Us</li></ul>
  </div>
  <div class="foot-col" style="left:617px;height:130px">
    <h4 style="margin-top:6px">Resources</h4>
    <ul><li>Teeth Cleaning</li><li>Whitening</li><li>Implantology</li><li>Root Canal</li><li>Clear Aligners</li></ul>
  </div>
  <div class="foot-col" style="left:830px;height:30px">
    <h4>Contact Us</h4>
    <div class="contact-row"><span class="dot-ico"><svg width="12" height="12" viewBox="0 0 24 24"><path fill="#fff" d="M12 2a7 7 0 00-7 7c0 5 7 13 7 13s7-8 7-13a7 7 0 00-7-7zm0 9.5a2.5 2.5 0 110-5 2.5 2.5 0 010 5z"/></svg></span><span>Linden Lane 12<br>4821 BK Ashford</span></div>
    <div class="contact-row"><span class="dot-ico"><svg width="12" height="12" viewBox="0 0 24 24"><path fill="#fff" d="M6.6 10.8a15 15 0 006.6 6.6l2.2-2.2c.3-.3.7-.4 1-.2 1.1.4 2.3.6 3.6.6.6 0 1 .4 1 1V20c0 .6-.4 1-1 1C10.6 21 3 13.4 3 4c0-.6.4-1 1-1h3.5c.6 0 1 .4 1 1 0 1.3.2 2.5.6 3.6.1.3 0 .7-.2 1z"/></svg></span><span>+1 555 014 2290</span></div>
    <div class="contact-row"><span class="dot-ico"><svg width="12" height="12" viewBox="0 0 24 24"><path fill="#fff" d="M3 5h18v14H3zm2 2v.5l7 5 7-5V7z"/></svg></span><span>hello@maplegrovedental.com</span></div>
  </div>
  <div class="abs" style="left:0;top:3790px;width:1200px;height:1px;background:#e3e6e8"></div>
  <div class="copyright">Copyright © 2022 Maple Grove | All Rights Reserved</div>
</footer>

</body>
</html>
```